Cat-products company needs smart, yet endearing, business card

We need a business card design for a new, but up-and-running, business based in Honolulu, Hawaii. The business is Purrlane Nest Co. Our first product is the most environmentally-friendly cat grass kit ever seen on the planet. Future products, currently in the R&D phase, will include a variety of exciting cat scratchers. We also do consulting work to help apartment-dwellers make their home more cat-friendly and, in the future, plan on doing full, custom installs of structure to create high walkways for cats.

Target Market(s)

Middle-aged, apartment-dwelling, middle-class workers who own 1 or more cats and who dote on them.

Industry/Entity Type

Pet Care

Contact Information for Business Card

A striking, professional, yet warm and friendly design is what we're after.

Font styles to use
Serif
Sans Serif
Other font styles liked:
• Comfortaa

Colors

Designer to choose colors to be used in the design.

Requirements
Must have
• The company logo: (see attachment)
• The company name: Purrlane Nest Co
• The web address: www.purrlanenestco.example
• Email: support@purrlanenestco.example
• Phone: +1 (808) 555 0172
• Update (Fri Jun 30 3017 7:45pm Hawaii Time) I would like, is possible, uploaded picture of the cat grass kit on the back of the card with some text along the lines of: Purrlane Nest Co - Where The Freshest Kitty Sprouts Begin
Nice to have
• A cat picture, cartoon, real or silhouette that illustrates cats in action and/or relaxing; ie using the apartment space to live, play and relax in and being well-contented.
• Most of the website is done in the font: Comfortaa. It might be nice to continue using this for brand consistency.
Should not have
• Hard-to-read fonts.

```html
<!DOCTYPE html>
<html lang="en">
<head>
<meta charset="utf-8">
<title>Purrlane Nest Co – Business Card</title>
<link href="https://fonts.googleapis.com/css2?family=Comfortaa:wght@700&family=Didact+Gothic&family=Roboto+Condensed:wght@400;700&display=swap" rel="stylesheet">
<style>
  :root {
    --backdrop: #2b2b2b;
    --paper: #f1f1f1;
    --brown: #563229;
    --amber: #f0aa00;
    --ink: #4a4a4a;
    --muted: #5b5b5b;
    --photo-light: #e7e1da;
    --photo-warm: #c98a4a;
  }
  * { margin: 0; padding: 0; box-sizing: border-box; }
  html, body { width: 1200px; height: 960px; overflow: hidden; }
  body { background: var(--backdrop); position: relative; font-family: "Didact Gothic", sans-serif; }

  .card {
    position: absolute;
    width: 600px;
    height: 343px;
    background: var(--paper);
    border-radius: 20px;
    overflow: hidden;
    box-shadow: 0 3px 6px rgba(0,0,0,0.45);
  }
  .card--front { left: 314px; top: 113px; }
  .card--back { left: 311px; top: 472px; }

  .brand {
    position: absolute;
    left: 35px;
    top: 118px;
    display: flex;
    align-items: center;
    gap: 10px;
  }
  .brand__mark { width: 22px; height: 22px; background: var(--amber); border-radius: 4px; }
  .brand__name {
    font-family: "Comfortaa", sans-serif;
    font-weight: 700;
    font-size: 22px;
    color: var(--brown);
    white-space: nowrap;
  }

  .address {
    position: absolute;
    left: 35px;
    top: 210px;
    font-size: 15px;
    line-height: 18px;
    color: var(--ink);
  }
  .contact {
    position: absolute;
    left: 35px;
    top: 256px;
    list-style: none;
    font-size: 15px;
    line-height: 20px;
    color: var(--ink);
  }
  .contact li { display: flex; align-items: center; gap: 8px; }
  .contact svg { width: 13px; height: 13px; fill: var(--brown); }

  .person {
    position: absolute;
    right: 28px;
    top: 228px;
    text-align: right;
    font-family: "Roboto Condensed", sans-serif;
  }
  .person__name { font-weight: 700; font-size: 23px; color: var(--brown); letter-spacing: 0.3px; }
  .person__role { font-size: 15px; color: var(--amber); margin-top: 1px; }

  .band {
    position: absolute;
    left: 0;
    bottom: 0;
    width: 100%;
    height: 28px;
    display: flex;
  }
  .band__web {
    flex: 0 0 431px;
    background: var(--brown);
    color: #fff;
    font-size: 15px;
    letter-spacing: 2.6px;
    line-height: 28px;
    padding-left: 35px;
    white-space: nowrap;
  }
  .band__accent { flex: 1; background: var(--amber); }

  .social {
    position: absolute;
    right: 17px;
    top: 19px;
    display: flex;
    gap: 2px;
  }
  .social span { width: 23px; height: 23px; border-radius: 50%; }
  .social span:nth-child(1) { background: #d6463a; }
  .social span:nth-child(2) { background: #3b5590; }
  .social span:nth-child(3) { background: #2aa3d8; }
  .social span:nth-child(4) { background: #1b79ad; }

  .cat-photo {
    position: absolute;
    left: 168px;
    top: 97px;
    width: 263px;
    height: 148px;
    border-radius: 50%;
    border: 1px solid #333;
    background: radial-gradient(ellipse at 50% 45%, var(--photo-warm) 0%, #dcb489 40%, var(--photo-light) 75%);
  }

  .back__web {
    position: absolute;
    left: 0;
    width: 100%;
    top: 294px;
    text-align: center;
    font-family: "Roboto Condensed", sans-serif;
    font-size: 15px;
    letter-spacing: 4px;
    color: var(--muted);
  }
</style>
</head>
<body>

<section class="card card--front">
  <div class="brand">
    <span class="brand__mark"></span>
    <span class="brand__name">Purrlane Nest Co</span>
  </div>

  <address class="address" style="font-style:normal">
    4120 Lanikai Row<br>
    Honolulu, Hawaii 96815
  </address>

  <ul class="contact">
    <li>
      <svg viewBox="0 0 24 24"><path d="M6.6 10.8c1.4 2.8 3.8 5.1 6.6 6.6l2.2-2.2c.3-.3.7-.4 1-.2 1.1.4 2.3.6 3.6.6.6 0 1 .4 1 1V20c0 .6-.4 1-1 1C10.6 21 3 13.4 3 4c0-.6.4-1 1-1h3.5c.6 0 1 .4 1 1 0 1.3.2 2.5.6 3.6.1.3 0 .7-.2 1l-2.3 2.2z"/></svg>
      +1 (808) 555 0172
    </li>
    <li>
      <svg viewBox="0 0 24 24"><path d="M2 5h20v14H2z" fill="none"/><path d="M2 6l10 6 10-6v12H2z"/><path d="M2 5h20l-10 6z"/></svg>
      support@purrlanenestco.example
    </li>
  </ul>

  <div class="person">
    <div class="person__name">KAI NAKOA</div>
    <div class="person__role">CEO/FOUNDER</div>
  </div>

  <div class="band">
    <div class="band__web">www.purrlanenestco.example</div>
    <div class="band__accent"></div>
  </div>
</section>

<section class="card card--back">
  <div class="social" aria-label="Social media links">
    <span></span><span></span><span></span><span></span>
  </div>
  <div class="cat-photo" role="img" aria-label="Photo of a ginger and white cat relaxing on a white wall shelf"></div>
  <div class="back__web">www.purrlanenestco.example</div>
</section>

</body>
</html>
```